VANTO Redesign

Make a more modern looking Homepage. Our page: www.vanto.at
Should look like:
www.kerno.com/at/de/
https://web.pallvik.com
https://id.montcalvet.com

Target Market(s)

furniture industry

Number of Pages Required

1 page

Font styles to use
Sans Serif

Colors
3176b5

```html
<!DOCTYPE html>
<html lang="en">
<head>
<meta charset="utf-8">
<title>VANTO – Fashion for Furniture</title>
<link href="https://fonts.googleapis.com/css2?family=Roboto:wght@400;500;700;900&family=Poppins:wght@400;500;600&display=swap" rel="stylesheet">
<style>
:root{
  --navy:#0d1f63;
  --navy-deep:#0a1a52;
  --blue:#3176b5;
  --blue-bright:#2f6fcf;
  --ink:#1a1a1a;
  --text:#444;
  --grey-bg:#f1f1f1;
  --line:#dcdcdc;
  --white:#fff;
}
*{box-sizing:border-box;margin:0;padding:0}
html,body{width:1200px;height:4852px;overflow:hidden}
body{font-family:"Poppins",sans-serif;color:var(--text);background:var(--white);position:relative}
.abs{position:absolute}
section,header,footer{position:absolute;left:0;width:1200px}

/* header */
.site-header{top:0;height:130px;background:var(--navy);color:var(--white)}
.brand{left:123px;top:22px;display:flex;align-items:center;gap:14px}
.brand-dot{width:46px;height:46px;border-radius:50%;background:var(--white)}
.brand-name{font-family:"Roboto",sans-serif;font-weight:700;font-size:50px;letter-spacing:6px;line-height:1}
.brand-tag{left:183px;top:82px;font-size:10px;letter-spacing:1px;opacity:.85}
.phone{left:505px;top:28px;display:flex;align-items:center;gap:10px;font-family:"Roboto",sans-serif;font-weight:700;font-size:19px}
.ico-round{width:30px;height:30px;border:2px solid var(--white);border-radius:50%;display:flex;align-items:center;justify-content:center}
.pill{top:24px;height:36px;border:2px solid var(--white);border-radius:18px;font-size:13px;font-weight:600;display:flex;align-items:center;justify-content:center;gap:6px;font-family:"Roboto",sans-serif}
.pill.login{left:754px;width:118px}
.pill.register{left:886px;width:124px}
.lang{left:1025px;top:27px;display:flex;align-items:center;gap:8px}
.flag{width:28px;height:28px;border-radius:50%;background:linear-gradient(90deg,var(--blue) 40%,#d22 40%,#d22 60%,var(--blue) 60%)}
.main-nav{top:82px;left:443px;display:flex;gap:0;font-family:"Roboto",sans-serif;font-weight:700;font-size:16px}
.main-nav a{color:var(--white);text-decoration:none;position:absolute;white-space:nowrap}

/* hero */
.hero{top:130px;height:600px;overflow:hidden}
.hero-photo{position:absolute;inset:0;background:linear-gradient(100deg,#6e6e6e 0%,#a9a9a9 35%,#cfcfcf 60%,#8b8b8b 100%)}
.hero h1{position:absolute;left:142px;top:150px;font-family:"Roboto",sans-serif;font-weight:900;font-size:48px;color:var(--white);letter-spacing:.5px}
.hero p{position:absolute;left:142px;color:var(--white);font-size:28px;font-weight:500;line-height:1.35}
.btn{display:flex;align-items:center;justify-content:center;border-radius:26px;color:var(--white);font-family:"Roboto",sans-serif;font-weight:700;font-size:16px;letter-spacing:.5px}
.hero .btn{position:absolute;left:146px;top:332px;width:196px;height:48px;background:var(--blue-bright)}
.hero-arrow{position:absolute;top:244px;width:34px;height:34px;border-radius:50%;background:#333;display:flex;align-items:center;justify-content:center}
.hero-curve{position:absolute;left:0;bottom:0}

/* section headings */
.sec-mark{width:28px;height:28px;border-radius:50%;background:var(--blue);left:586px}
.sec-title{left:0;width:1200px;text-align:center;font-family:"Roboto",sans-serif;font-weight:700;font-size:38px;color:var(--ink)}
.sec-title .light{font-weight:400}

/* welcome */
.welcome{top:730px;height:612px}
.welcome .intro{left:180px;width:840px;top:188px;text-align:center;font-size:14px;line-height:2.2;color:#555}
.feature{top:331px;width:217px;height:161px;background:var(--white);border:1px solid var(--line);box-shadow:0 3px 10px rgba(0,0,0,.12);text-align:center}
.feature svg{margin-top:26px}
.feature span{position:absolute;left:0;right:0;bottom:24px;font-family:"Roboto",sans-serif;font-weight:700;font-size:14px;color:var(--ink)}

/* products */
.products{top:1342px;height:980px;background:var(--grey-bg)}
.product{width:284px}
.product .photo{height:210px;border-bottom:5px solid var(--blue)}
.product h3{margin-top:28px;text-align:center;font-family:"Roboto",sans-serif;font-weight:700;font-size:14px;color:var(--ink)}
.product p{margin-top:10px;text-align:center;font-size:13px;line-height:1.9;color:#555}

/* video + configurator */
.video{top:2322px;height:1145px}
.video .blue-band{left:0;top:524px;width:1200px;height:621px;background:linear-gradient(180deg,#2f70c4,#2a65b2)}
.video .lede{left:340px;width:520px;top:196px;text-align:center;font-size:17px;line-height:1.7;color:#222}
.video-frame{left:146px;top:298px;width:906px;height:446px;border:5px solid var(--white);box-shadow:0 8px 24px rgba(0,0,0,.35);background:linear-gradient(120deg,#3a3a3a,#7a5a48 45%,#9c9c9c 70%,#2c2c2c)}
.play{left:52%;top:50%;transform:translate(-50%,-50%);width:76px;height:46px;background:#111;border-radius:6px;display:flex;align-items:center;justify-content:center}
.config-title{top:846px;left:0;width:1200px;text-align:center;font-family:"Roboto",sans-serif;font-weight:700;font-size:38px;color:var(--white)}
.config-sub{top:916px;left:0;width:1200px;text-align:center;font-size:22px;color:var(--white)}
.video .btn{position:absolute;left:494px;top:985px;width:212px;height:46px;border:2px solid var(--white)}

/* blog */
.blog{top:3467px;height:705px}
.post{top:226px;width:440px;height:301px}
.post .photo{height:301px}
.post-card{position:absolute;left:70px;top:214px;width:300px;height:136px;background:var(--white);box-shadow:0 4px 14px rgba(0,0,0,.15);text-align:center;padding-top:24px}
.post-card h3{font-size:16px;font-weight:400;line-height:1.55;color:#222}
.post-meta{margin-top:14px;display:flex;justify-content:center;gap:14px;font-size:12px;color:var(--blue)}

/* brands */
.brands{top:4172px;height:194px;background:var(--grey-bg)}
.brands ul{list-style:none;position:absolute;left:160px;top:72px;width:880px;display:flex;justify-content:space-between;align-items:center}
.brands li{font-family:"Roboto",sans-serif;font-weight:700;font-size:28px;color:#9a9a9a}

/* footer */
.site-footer{top:4366px;height:486px;background:var(--navy);color:var(--white)}
.footer-curve{left:0;top:-60px}
.site-footer h4{font-family:"Roboto",sans-serif;font-weight:700;font-size:22px;position:absolute}
.contact-list{left:142px;top:124px;list-style:none;font-size:13px;line-height:1.55}
.contact-list li{display:flex;gap:14px;margin-bottom:14px}
.links{left:432px;top:124px;list-style:none;font-size:13px;line-height:2.05}
.links li::before{content:"";display:inline-block;width:8px;height:8px;border-radius:50%;background:var(--white);margin-right:12px;vertical-align:middle}
.news-label{left:670px;top:130px;font-size:13px}
.news-input{left:670px;top:166px;width:258px;height:34px;background:var(--white);color:#888;font-size:11px;padding:10px 14px}
.news-btn{left:938px;top:166px;width:113px;height:34px;background:var(--blue);font-family:"Roboto",sans-serif;font-weight:700;font-size:12px;display:flex;align-items:center;justify-content:center}
.hours{left:670px;top:220px;font-size:12px;line-height:1.75}
.hours strong{font-family:"Roboto",sans-serif;font-size:13px;display:block;margin-bottom:6px}
.social{left:880px;top:268px;display:flex;gap:10px}
.social span{width:34px;height:34px;border:2px solid var(--white);border-radius:50%}
.bottom-bar{left:0;top:388px;width:1200px;height:98px;border-top:1px solid rgba(255,255,255,.25);background:var(--navy-deep);text-align:center;font-size:13px;padding-top:36px}
</style>
</head>
<body>

<header class="site-header">
  <div class="abs brand"><span class="brand-dot"></span><span class="brand-name">VANTO</span></div>
  <div class="abs brand-tag">FASHION FOR FURNITURE</div>
  <div class="abs phone">
    <span class="ico-round"><svg width="14" height="14" viewBox="0 0 24 24"><path fill="#fff" d="M6.6 10.8a15 15 0 0 0 6.6 6.6l2.2-2.2a1 1 0 0 1 1-.25 11.4 11.4 0 0 0 3.6.57 1 1 0 0 1 1 1V20a1 1 0 0 1-1 1A17 17 0 0 1 3 4a1 1 0 0 1 1-1h3.5a1 1 0 0 1 1 1c0 1.25.2 2.45.57 3.6a1 1 0 0 1-.25 1z"/></svg></span>
    +43 (0) 7100 4410-0
  </div>
  <div class="abs pill login"><svg width="13" height="13" viewBox="0 0 24 24"><circle cx="12" cy="8" r="5" fill="#fff"/><path d="M3 22a9 9 0 0 1 18 0z" fill="#fff"/></svg>LOGIN</div>
  <div class="abs pill register"><svg width="13" height="13" viewBox="0 0 24 24"><path d="M3 17v4h4L19 9l-4-4z" fill="#fff"/></svg>REGISTER</div>
  <div class="abs lang"><span class="flag"></span><svg width="10" height="8" viewBox="0 0 10 8"><path d="M1 1l4 5 4-5" stroke="#fff" stroke-width="1.6" fill="none"/></svg></div>
  <nav class="abs main-nav">
    <a style="left:0">BRAND NEW</a>
    <a style="left:133px">CATALOG CONFIGURATOR</a>
    <a style="left:375px">LIGHT CONFIGURATOR</a>
    <a style="left:585px">LAMP</a>
  </nav>
</header>

<section class="hero">
  <div class="hero-photo" role="img" aria-label="Close-up of a brushed steel bar handle on a grey wood-grain cabinet door"></div>
  <h1>FURNITURE FITTINGS</h1>
  <p style="top:222px">Functionality meets Design.</p>
  <p style="top:262px">Be inspired by the new VANTO-Collection.</p>
  <div class="btn">GET MORE INFO</div>
  <div class="hero-arrow" style="left:70px"><svg width="12" height="12" viewBox="0 0 12 12"><path d="M8 1L3 6l5 5" stroke="#fff" stroke-width="2" fill="none"/></svg></div>
  <div class="hero-arrow" style="left:1092px"><svg width="12" height="12" viewBox="0 0 12 12"><path d="M4 1l5 5-5 5" stroke="#fff" stroke-width="2" fill="none"/></svg></div>
  <svg class="hero-curve" width="1200" height="140" viewBox="0 0 1200 140">
    <path d="M0 20 Q600 150 1200 20 L1200 140 L0 140Z" fill="#fff"/>
    <path d="M70 62 Q600 150 1130 62" stroke="var(--blue-bright)" stroke-width="8" fill="none" stroke-linecap="round"/>
    <path d="M0 20 Q600 150 1200 20" stroke="#fff" stroke-width="4" fill="none"/>
  </svg>
</section>

<section class="welcome">
  <h2 class="abs sec-title" style="top:118px">WELCOME TO <span class="light">VANTO</span></h2>
  <p class="abs intro">Sed ut perspiciatis unde omnis iste natus error sit voluptatem accusantium doloremque laudantium, totam rem aperiam, eaque ipsa quae ab illo inventore veritatis et quasi architecto beatae vitae dicta sunt explicabo. Nemo enim ipsam voluptatem quia voluptas sit aspernatur aut odit aut fugit, sed quia consequuntur magni dolores eos qui ratione</p>
  <div class="abs feature" style="left:142px">
    <svg width="74" height="74" viewBox="0 0 74 74"><circle cx="37" cy="37" r="34" stroke="var(--blue)" stroke-width="3" fill="none"/><path d="M37 20v24M27 35l10 10 10-10M24 50h26" stroke="var(--blue)" stroke-width="3" fill="none" stroke-linecap="round"/></svg>
    <span>CATALOG / DOWNLOADS</span>
  </div>
  <div class="abs feature" style="left:375px">
    <svg width="74" height="74" viewBox="0 0 74 74"><circle cx="37" cy="37" r="34" stroke="var(--blue)" stroke-width="3" fill="none"/><path d="M24 24l26 26M50 24L24 50" stroke="var(--blue)" stroke-width="4" stroke-linecap="round"/></svg>
    <span>INSTALLATION</span>
  </div>
  <div class="abs feature" style="left:608px">
    <svg width="74" height="74" viewBox="0 0 74 74"><circle cx="37" cy="37" r="34" stroke="var(--blue)" stroke-width="3" fill="none"/><circle cx="37" cy="34" r="12" stroke="var(--blue)" stroke-width="3" fill="none"/><path d="M31 50h12" stroke="var(--blue)" stroke-width="3" stroke-linecap="round"/></svg>
    <span>LIGHT CONFIGURATOR</span>
  </div>
  <div class="abs feature" style="left:841px">
    <svg width="74" height="74" viewBox="0 0 74 74"><circle cx="37" cy="37" r="34" stroke="var(--blue)" stroke-width="3" fill="none"/><path d="M27 40h20l-4-18h-12z" stroke="var(--blue)" stroke-width="3" fill="none"/><path d="M37 40v10" stroke="var(--blue)" stroke-width="3"/></svg>
    <span>LAMP</span>
  </div>
</section>

<section class="products">
  <span class="abs sec-mark" style="top:60px"></span>
  <h2 class="abs sec-title" style="top:106px">PRODUCT CATALOG</h2>
  <div class="abs product" style="left:146px;top:201px"><div class="photo" role="img" aria-label="Glass shop front with dark metal door frames" style="background:linear-gradient(160deg,#1d2c44,#4d6079 50%,#20283a)"></div><h3>QUIS AUTEM VEL EUM IURE</h3><p>Sed ut perspiciatis unde omnis iste natus error sit voluptatem accusantium</p></div>
  <div class="abs product" style="left:456px;top:201px"><div class="photo" role="img" aria-label="Glass door with tall steel pull handles in a bright lobby" style="background:linear-gradient(160deg,#c8d0c0,#eef0ea 50%,#9aa69a)"></div><h3>QUIS AUTEM VEL EUM IURE</h3><p>Sed ut perspiciatis unde omnis iste natus error sit voluptatem accusantium</p></div>
  <div class="abs product" style="left:770px;top:201px"><div class="photo" role="img" aria-label="Chrome lever handle on a light oak door" style="background:linear-gradient(160deg,#c99a68,#e0b987 50%,#a7784a)"></div><h3>QUIS AUTEM VEL EUM IURE</h3><p>Sed ut perspiciatis unde omnis iste natus error sit voluptatem accusantium</p></div>
  <div class="abs product" style="left:146px;top:560px"><div class="photo" role="img" aria-label="Brass lever handle on a reddish wooden door" style="background:linear-gradient(160deg,#7a3a1e,#a95c2e 50%,#6a2f18)"></div><h3>QUIS AUTEM VEL EUM IURE</h3><p>Sed ut perspiciatis unde omnis iste natus error sit voluptatem accusantium</p></div>
  <div class="abs product" style="left:456px;top:560px"><div class="photo" role="img" aria-label="Ornate gold door handles on a dark wooden double door" style="background:linear-gradient(160deg,#3a1e10,#6e4418 50%,#2c160a)"></div><h3>QUIS AUTEM VEL EUM IURE</h3><p>Sed ut perspiciatis unde omnis iste natus error sit voluptatem accusantium</p></div>
  <div class="abs product" style="left:770px;top:560px"><div class="photo" role="img" aria-label="Round door knob with a hanging sign on a dark wooden door" style="background:linear-gradient(160deg,#4a2516,#7a4028 50%,#3a1c10)"></div><h3>QUIS AUTEM VEL EUM IURE</h3><p>Sed ut perspiciatis unde omnis iste natus error sit voluptatem accusantium</p></div>
</section>

<section class="video">
  <div class="abs blue-band"></div>
  <span class="abs sec-mark" style="top:68px"></span>
  <h2 class="abs sec-title" style="top:126px">WATCH THE VANTO VIDEO</h2>
  <p class="abs lede">The new vintage colours create a fresh look for long established items and give furniture new character.</p>
  <div class="abs video-frame" role="img" aria-label="Trade fair stand with visitors browsing illuminated displays of handles">
    <div class="abs play"><svg width="20" height="20" viewBox="0 0 20 20"><path d="M5 3l12 7-12 7z" fill="#fff"/></svg></div>
  </div>
  <h2 class="abs config-title">CATALOG CONFIGURATOR</h2>
  <p class="abs config-sub">Creating A Collection | Catalogue - This Is How It Works</p>
  <div class="btn">GET MORE INFO</div>
</section>

<section class="blog">
  <span class="abs sec-mark" style="top:74px"></span>
  <h2 class="abs sec-title" style="top:122px">LATEST BLOG</h2>
  <article class="abs post" style="left:142px">
    <div class="photo" role="img" aria-label="Drawer fronts and handle samples laid out on a wooden table" style="background:linear-gradient(160deg,#6a3a20,#c8c2b8 50%,#8a5a34)"></div>
    <div class="post-card"><h3>Sed ut perspiciatis unde omnis sit<br>voluptatem accusantium</h3><div class="post-meta"><span>&#9635; Jan 25, 2018</span><span>|</span><span>&#9675; 3 comments</span></div></div>
  </article>
  <article class="abs post" style="left:618px">
    <div class="photo" role="img" aria-label="Warmly lit kitchen cabinets with under-shelf lighting" style="background:linear-gradient(160deg,#6a3a18,#e0b07a 45%,#f3dcc0 60%,#8a5228)"></div>
    <div class="post-card"><h3>Sed ut perspiciatis unde omnis sit<br>voluptatem accusantium</h3><div class="post-meta"><span>&#9635; Jan 25, 2018</span><span>|</span><span>&#9675; 3 comments</span></div></div>
  </article>
</section>

<section class="brands">
  <ul><li>TRAVEK</li><li>Aumera</li><li>LEGATO</li><li>Ovento</li><li>verdo</li><li>FOLMAR</li></ul>
</section>

<footer class="site-footer">
  <svg class="abs footer-curve" width="1200" height="120" viewBox="0 0 1200 120">
    <path d="M0 0 L1200 0 L1200 60 Q600 -10 0 60Z" fill="var(--grey-bg)"/>
    <path d="M60 52 Q600 -8 1140 52" stroke="var(--blue-bright)" stroke-width="6" fill="none" stroke-linecap="round"/>
  </svg>
  <h4 style="left:142px;top:70px">CONTACT US</h4>
  <ul class="abs contact-list">
    <li><span>&#9679;</span><span>VANTO Beschläge<br>Lindenweg 8<br>4850 Ahrberg Austria</span></li>
    <li><span>&#9742;</span><span>Phone: +43 (0) 7100 4410-0</span></li>
    <li><span>&#9112;</span><span>Fax: +43 (0) 7100 4412</span></li>
    <li><span>&#9993;</span><span>E-Mail: office@vanto.at</span></li>
  </ul>
  <h4 style="left:432px;top:70px">QUICK LINKS</h4>
  <ul class="abs links">
    <li>Home</li><li>Catalog / Downloads</li><li>About Us</li><li>Exhibition Dates</li><li>Privacy Policy</li><li>Imprint</li><li>Contact</li>
  </ul>
  <h4 style="left:670px;top:70px">SIGN UP FOR NEWSLETTER</h4>
  <p class="abs news-label">Sign up to our mailing list</p>
  <div class="abs news-input">Enter email</div>
  <div class="abs news-btn">SUBSCRIPTION</div>
  <div class="abs hours"><strong>OFFICE HOURS</strong>Mon - thu: 07:30 - 12:00<br>Mon - thu: 12:30 - 16:30<br>Fri: 07:30 - 12:00</div>
  <div class="abs social"><span></span><span></span><span></span><span></span></div>
  <div class="abs bottom-bar">(c) 2019 VANTO | All Rights Reserved | Disclaimer</div>
</footer>

</body>
</html>
```